Business Card Design

We need a business card to highlight our property maintenance company. we specialize in commercial and industrial property maintenance. services include landscaping snow and ice management. janitorial services. cleanroom services. parking lot maintenance.
Updates
I have narrowed down to two designs thank you waiting on some minor changes to both designs to choose.
Target Market(s)
facility managers/property managers
Industry/Entity Type
Property Maintenance
Contact Information for Business Card
47 Brindlewood Rd.
Halden, Ma. 01839
978-552-3716
Look and feel

```html
<!DOCTYPE html>
<html lang="en">
<head>
<meta charset="UTF-8">
<title>Keystone Property Services – Business Card</title>
<link rel="stylesheet" href="https://fonts.googleapis.com/css2?family=Cinzel:wght@600;700&family=Roboto:wght@400;900&display=swap">
<style>
  :root {
    --navy: #15185a;
    --gold: #f4c91c;
    --paper: #ffffff;
    --paper-shade: #f1f1f3;
    --ghost: #ece9da;
    --backdrop: #e8e5e0;
  }
  * { margin: 0; padding: 0; box-sizing: border-box; }
  html, body { width: 1200px; height: 784px; overflow: hidden; }
  body { background: var(--backdrop); position: relative; font-family: "Roboto", Arial, sans-serif; }

  .card {
    position: absolute;
    top: 237px;
    width: 540px;
    height: 309px;
    background: linear-gradient(160deg, var(--paper) 0%, var(--paper-shade) 100%);
    box-shadow: 0 6px 18px rgba(0,0,0,0.18);
    overflow: hidden;
  }
  .card--back { left: 40px; }
  .card--front { left: 620px; }

  .card__art { position: absolute; inset: 0; width: 100%; height: 100%; }

  .back-mark {
    position: absolute;
    inset: 0;
    display: flex;
    align-items: center;
    justify-content: center;
    font-family: "Roboto", Arial, sans-serif;
    font-weight: 900;
    font-size: 86px;
    color: var(--ghost);
    letter-spacing: 1px;
  }

  .brand {
    position: absolute;
    left: 30px;
    top: 112px;
    color: var(--navy);
  }
  .brand__name {
    display: flex;
    align-items: center;
    gap: 8px;
    font-family: "Roboto", Arial, sans-serif;
    font-weight: 900;
    font-size: 30px;
    line-height: 1;
    color: var(--navy);
  }
  .brand__square { width: 22px; height: 22px; background: var(--gold); }
  .brand__tagline {
    margin-top: 8px;
    font-family: "Cinzel", serif;
    font-weight: 700;
    font-size: 15px;
    line-height: 1.15;
    letter-spacing: 0.5px;
  }

  .contact {
    position: absolute;
    left: 318px;
    top: 190px;
    list-style: none;
    color: var(--paper);
    font-size: 15px;
    line-height: 1.3;
    white-space: nowrap;
  }
  .contact__item { display: flex; align-items: flex-start; gap: 5px; }
  .contact__icon { width: 15px; height: 15px; margin-top: 2px; flex: none; }
  .contact__item--address span { display: block; }
</style>
</head>
<body>

  <section class="card card--back" aria-label="Business card, back">
    <div class="back-mark">Keystone</div>
  </section>

  <section class="card card--front" aria-label="Business card, front">
    <svg class="card__art" viewBox="0 0 540 309" preserveAspectRatio="none" aria-hidden="true">
      <path class="swoosh" fill="var(--gold)" d="M318,166 C420,128 492,76 522,0 L532,0 C506,80 430,135 318,166 Z"/>
      <path class="navy-field" fill="var(--navy)" d="M40,309 C190,262 360,205 448,128 C500,82 525,40 540,8 L540,309 Z"/>
    </svg>

    <div class="brand">
      <div class="brand__name"><span class="brand__square"></span>Keystone</div>
      <div class="brand__tagline">Property Services<br>Halden, Ma</div>
    </div>

    <ul class="contact">
      <li class="contact__item">
        <svg class="contact__icon" viewBox="0 0 24 24" aria-hidden="true"><path fill="var(--gold)" d="M6.6 10.8a15.1 15.1 0 0 0 6.6 6.6l2.2-2.2c.3-.3.7-.4 1-.2 1.1.4 2.3.6 3.6.6.6 0 1 .4 1 1V20c0 .6-.4 1-1 1A17 17 0 0 1 3 4c0-.6.4-1 1-1h3.5c.6 0 1 .4 1 1 0 1.3.2 2.5.6 3.6.1.3 0 .7-.2 1l-2.3 2.2z"/></svg>
        978-552-3716
      </li>
      <li class="contact__item contact__item--address">
        <svg class="contact__icon" viewBox="0 0 24 24" aria-hidden="true"><path fill="var(--gold)" d="M12 3 2 12h3v8h5v-6h4v6h5v-8h3z"/></svg>
        <div><span>47 Brindlewood Rd. Halden,</span><span>Ma. 01839</span></div>
      </li>
    </ul>
  </section>

</body>
</html>
```